Zerovan Medical

We are a medical supplier company we sell machines and equipment to all medical sectors in Iraq. Our services include not only the installation of these machines and equipment but also we provide support after installation and we train the staff to use these machines/equipment
We need a website that will make us stand out from our competitors, something professional and catchy
Starting from the home page, before showing the home page we want the loading screen to have our logo animated in a nice way
Then we can proceed to creating the other pages which are
Projects
Services
Training
About
and Contact us
Attached below is our logo and the color blue that we hope to use in the theme of the website
**** In the home page we want to focus on our partners and services****

Target Market(s)

Medical Sector

Industry/Entity Type

Medical

Coding

Coded - Design and coding required

Number of Pages Required

5+ page

Colors
0054AA
0677BA
7BADD7
CADEEF
E8F1F8

Requirements
Must have
• Animation in loading screen or animation in home page
Nice to have
• Some sort of animation for our partners

```html
<!DOCTYPE html>
<html lang="en">
<head>
<meta charset="utf-8">
<title>Zerovan Medical — Medical Equipment Supplier in Iraq</title>
<link rel="stylesheet" href="https://fonts.googleapis.com/css2?family=Poppins:wght@400;500;600;700&family=Fira+Sans:wght@600;700&display=swap">
<style>
:root{
  --navy:#24296b;
  --navy-deep:#1d2260;
  --blue:#2b9ad7;
  --blue-bright:#1f8fd3;
  --hero-blue:#1e5ba8;
  --ice:#e8f1f8;
  --ice-2:#cadeef;
  --sky:#7badd7;
  --ink:#24296b;
  --text:#3d4266;
  --white:#ffffff;
  --line:#d7e3ee;
}
*{box-sizing:border-box;margin:0;padding:0}
html,body{width:1200px;height:4996px;overflow:hidden}
body{position:relative;font-family:"Poppins",sans-serif;color:var(--text);background:var(--white)}
.section{position:absolute;left:0;width:1200px;overflow:hidden}
.abs{position:absolute}
.center{left:0;width:1200px;text-align:center}
.btn{position:absolute;display:flex;align-items:center;justify-content:center;font-family:"Poppins",sans-serif;font-weight:500;font-size:11px;letter-spacing:.3px;text-transform:uppercase}
.btn-navy{background:var(--navy);color:var(--white)}
.btn-white{background:var(--white);color:var(--navy)}
.btn-outline{border:1.5px solid var(--navy);color:var(--navy);background:var(--white)}
.btn-blue{background:var(--blue);color:var(--white)}
.btn-notch::after{content:"";position:absolute;right:-8px;top:-6px;width:22px;height:calc(100% + 12px);border:1.5px solid rgba(255,255,255,.45);border-left:none}
.sec-title{position:absolute;font-weight:700;font-size:37px;color:var(--ink);letter-spacing:.3px;line-height:40px}
.sec-sub{position:absolute;font-size:13px;color:var(--blue);text-transform:uppercase;letter-spacing:.2px}
.sec-rule{position:absolute;left:553px;width:94px;height:2px;background:var(--blue)}

/* Header + hero */
.hero{top:0;height:650px;background:linear-gradient(180deg,#1f4f98 0%,#2466b1 55%,#2a73bb 100%)}
.hero-bg{position:absolute;inset:0;background:radial-gradient(ellipse at 50% 40%,rgba(90,150,215,.35),rgba(20,60,130,.0) 70%)}
.brand{position:absolute;display:flex;align-items:center;gap:10px;font-weight:600;font-size:24px;line-height:1;color:var(--white);white-space:nowrap}
.brand-mark{width:34px;height:34px;border:3px solid var(--white);flex:none}
.support{top:8px;left:630px;font-size:10px;font-weight:600;color:var(--white);display:flex;align-items:center;gap:6px}
.search{top:0;left:810px;width:247px;height:33px;background:var(--navy-deep);display:flex;align-items:center}
.search span{font-size:9px;color:#aab3d6;padding-left:16px;flex:1}
.search i{width:33px;height:33px;background:var(--sky);display:flex;align-items:center;justify-content:center}
.hero-title{top:182px;font-weight:700;font-size:42px;line-height:46px;color:var(--white)}
.hero-lead{top:286px;font-size:15px;color:#e1ecf8}
.machine{position:absolute;border-radius:18px;background:linear-gradient(180deg,rgba(235,243,250,.85),rgba(190,210,230,.75))}

/* Partners */
.partners{top:650px;height:120px;background:var(--white)}
.partner{position:absolute;top:35px;width:168px;height:85px;border:1px solid var(--line);background:var(--white);display:flex;align-items:center;justify-content:center;box-shadow:0 4px 10px rgba(30,60,120,.06)}
.partner i{display:block;background:var(--ice-2)}

/* Welcome */
.welcome{top:770px;height:500px;background:linear-gradient(90deg,#f4f8fb,#fff 40%)}
.welcome p{position:absolute;left:250px;width:700px;text-align:center;font-size:12.5px;line-height:23px;color:#3c4060}

/* Solutions */
.solutions{top:1270px;height:635px;background:var(--navy)}
.solutions .sec-title{color:var(--white)}
.solutions .sec-sub{color:var(--blue)}
.svc{position:absolute;width:239px;height:281px;background:var(--white);text-align:center}
.svc.active{background:var(--blue);color:var(--white)}
.svc svg{position:absolute;left:90px;top:42px}
.svc h3{position:absolute;left:0;width:100%;top:120px;font-family:"Fira Sans",sans-serif;font-weight:600;font-size:19px;color:var(--ink)}
.svc.active h3{color:var(--white)}
.svc p{position:absolute;left:25px;width:189px;top:160px;font-size:10.5px;line-height:16px;color:#555a78}
.svc.active p{color:#e7f3fb}
.svc .btn{left:61px;top:213px;width:118px;height:33px;font-size:10px}

/* Equipment */
.equipment{top:1905px;height:978px;background:var(--white)}
.equip{position:absolute;background:var(--ice);border:1px solid #dde9f3}
.equip .art{position:absolute;border-radius:12px;background:linear-gradient(180deg,#f7fafd,#c8d6e4)}
.equip h4{position:absolute;left:0;width:100%;text-align:center;font-family:"Fira Sans",sans-serif;font-weight:600;font-size:21px;color:var(--ink)}

/* Empowering */
.empower{top:2883px;height:475px;background:linear-gradient(90deg,#3a4f78 0%,#2c3d6a 40%,#1e2a5e 60%,#1a2358 100%)}
.empower h2{position:absolute;left:654px;top:96px;font-weight:700;font-size:58px;line-height:64px;color:var(--white)}
.empower p{position:absolute;left:656px;top:238px;width:420px;font-size:13.5px;line-height:22px;color:#e5ebf5;text-transform:uppercase}

/* Why */
.why{top:3358px;height:871px;background:var(--white)}
.feature{position:absolute;width:170px;text-align:center}
.feature .ico{width:58px;height:58px;margin:0 auto;border:2px solid var(--ice-2);background:#fff;display:flex;align-items:center;justify-content:center}
.feature .ico span{width:44px;height:44px;background:var(--navy);display:flex;align-items:center;justify-content:center}
.feature h5{margin-top:20px;font-weight:600;font-size:13px;line-height:18px;color:var(--ink);text-transform:uppercase}
.feature hr{border:none;height:1px;background:var(--line);width:150px;margin:14px auto 0}

/* CTA */
.cta{top:4229px;height:392px;background:linear-gradient(90deg,#1a86cc,#2596d8 50%,#1a86cc)}
.cta h2{top:86px;font-weight:700;font-size:46px;line-height:52px;color:var(--white)}
.cta p{top:208px;font-size:13.5px;color:var(--white);text-transform:uppercase}

/* Footer */
.footer{top:4621px;height:375px;background:var(--navy)}
.footer h6{position:absolute;top:88px;font-weight:600;font-size:14px;color:var(--blue);text-transform:uppercase}
.footer .links{position:absolute;left:417px;top:130px;font-size:10px;line-height:25px;color:#d3d7ee;list-style:none;text-transform:uppercase}
.social{position:absolute;top:144px;width:29px;height:29px;border:1px solid var(--blue);display:flex;align-items:center;justify-content:center}
.social i{width:9px;height:9px;background:var(--blue);border-radius:50%}
.contact-row{position:absolute;left:586px;display:flex;gap:12px;font-size:9.5px;color:#d3d7ee;line-height:14px}
.subscribe{position:absolute;left:828px;top:136px;width:231px;height:37px;border:1px solid #4a5090;display:flex;align-items:center}
.subscribe span{flex:1;font-size:9px;color:#9da3cd;padding-left:14px}
.subscribe i{width:36px;height:35px;background:var(--blue);display:flex;align-items:center;justify-content:center}
.copyright{top:343px;font-size:9.5px;color:#b7bcdf}
</style>
</head>
<body>

<header class="section hero">
  <div class="hero-bg" role="img" aria-label="Blurred hospital ward photograph in blue tones"></div>

  <div class="brand" style="left:140px;top:32px"><span class="brand-mark"></span>Zerovan Medical</div>

  <div class="abs support">
    <svg width="13" height="13" viewBox="0 0 24 24" fill="none" stroke="#fff" stroke-width="2.4"><path d="M4 14v-2a8 8 0 0 1 16 0v2"/><rect x="3" y="14" width="4" height="6" rx="1"/><rect x="17" y="14" width="4" height="6" rx="1"/></svg>
    SUPPORT :- 0770-555-0142
  </div>
  <div class="abs search"><span>Search...</span><i><svg width="12" height="12" viewBox="0 0 24 24" fill="none" stroke="#1d2260" stroke-width="3"><circle cx="10" cy="10" r="6"/><path d="M15 15l6 6"/></svg></i></div>

  <nav class="abs" style="top:56px;left:0;width:1200px;height:14px;font-size:10px;color:#fff;font-weight:500">
    <span class="abs" style="left:500px">HOME</span>
    <span class="abs" style="left:560px">ABOUT</span>
    <span class="abs" style="left:625px">SERVICES ⌄</span>
    <span class="abs" style="left:717px">TRAINING</span>
    <span class="abs" style="left:796px">PROJECTS</span>
    <span class="abs" style="left:884px;display:flex;align-items:center;gap:4px"><svg width="14" height="14" viewBox="0 0 24 24" fill="none" stroke="#fff" stroke-width="2"><circle cx="12" cy="12" r="9"/><path d="M3 12h18M12 3c3 3 3 15 0 18M12 3c-3 3-3 15 0 18"/></svg>ES ⌄</span>
  </nav>
  <div class="btn btn-white" style="left:947px;top:47px;width:112px;height:33px;font-size:9.5px">Contact Us</div>

  <h1 class="abs center hero-title">SUPPLYING THE<br>FUTURE OF MEDICAL IN IRAQ</h1>
  <p class="abs center hero-lead">Advanced Medical Machines &amp; Equipment with Full Support and Training</p>
  <div class="btn btn-white btn-notch" style="left:518px;top:332px;width:175px;height:44px">Go to Catalog</div>

  <div class="machine" style="left:40px;top:200px;width:275px;height:400px" role="img" aria-label="Anesthesia workstation product image"></div>
  <div class="machine" style="left:450px;top:440px;width:310px;height:180px;border-radius:40px" role="img" aria-label="Portable ventilator product image"></div>
  <div class="machine" style="left:865px;top:160px;width:280px;height:450px" role="img" aria-label="Dialysis machine product image"></div>
</header>

<section class="section partners" aria-label="Partners">
  <div class="partner" style="left:-50px"><i style="width:80px;height:26px"></i></div>
  <div class="partner" style="left:140px"><i style="width:34px;height:34px;border-radius:50%"></i></div>
  <div class="partner" style="left:330px"><i style="width:86px;height:40px"></i></div>
  <div class="partner" style="left:520px"><i style="width:110px;height:22px"></i></div>
  <div class="partner" style="left:712px"><i style="width:96px;height:30px"></i></div>
  <div class="partner" style="left:902px"><i style="width:56px;height:56px"></i></div>
  <div class="partner" style="left:1092px"><i style="width:90px;height:24px"></i></div>
</section>

<section class="section welcome">
  <h2 class="sec-title center" style="top:88px">WELCOME TO ZEROVAN</h2>
  <p class="sec-sub center" style="top:136px">Your Trusted Medical Equipment Partner</p>
  <span class="sec-rule" style="top:184px"></span>
  <p style="top:212px">At Zerovan Medical, we specialize in delivering cutting-edge medical equipment to healthcare facilities across Iraq. Our mission is to provide reliable solutions and ensure smooth integration through our comprehensive support and training services.</p>
  <p style="top:293px">Lorem ipsum dolor sit amet, consectetur adipiscing elit, sed do eiusmod tempor incididunt ut labore et dolore magna aliqua. Ut enim ad minim veniam, quis nostrud exercitation</p>
  <div class="btn btn-navy btn-notch" style="left:528px;top:365px;width:143px;height:41px">Learn More</div>
</section>

<section class="section solutions">
  <h2 class="sec-title center" style="top:88px">MEDICAL SOLUTIONS</h2>
  <p class="sec-sub center" style="top:136px">Our Services</p>

  <article class="svc" style="left:211px;top:259px">
    <svg width="60" height="60" viewBox="0 0 60 60" fill="none" stroke="#24296b" stroke-width="3"><path d="M10 50h40M18 50V38h24v12M22 38l8-14 8 14M30 24V12M24 12h12"/><circle cx="44" cy="18" r="5"/></svg>
    <h3>Installation</h3>
    <p>Seamless and efficient setup by expert technicians.</p>
    <div class="btn btn-outline">Know More</div>
  </article>

  <article class="svc active" style="left:481px;top:214px">
    <svg width="60" height="60" viewBox="0 0 60 60" fill="none" stroke="#fff" stroke-width="3"><path d="M12 30a18 18 0 0 1 36 0"/><rect x="8" y="28" width="8" height="14" rx="2"/><rect x="44" y="28" width="8" height="14" rx="2"/><circle cx="30" cy="32" r="10"/><circle cx="26" cy="32" r="1" fill="#fff"/><circle cx="30" cy="32" r="1" fill="#fff"/><circle cx="34" cy="32" r="1" fill="#fff"/></svg>
    <h3>Technical Support</h3>
    <p>Ongoing technical support to keep operations running smoothly.</p>
    <div class="btn btn-white" style="top:213px">Know More</div>
  </article>

  <article class="svc" style="left:751px;top:259px">
    <svg width="60" height="60" viewBox="0 0 60 60" fill="none" stroke="#24296b" stroke-width="3"><circle cx="20" cy="18" r="6"/><circle cx="40" cy="22" r="5"/><path d="M12 52V32a8 8 0 0 1 16 0v20M34 52V36a6 6 0 0 1 12 0v16"/><circle cx="40" cy="8" r="4"/></svg>
    <h3>Staff Training</h3>
    <p>In-depth training programs with the right knowledge and skills.</p>
    <div class="btn btn-outline">Know More</div>
  </article>
</section>

<section class="section equipment">
  <h2 class="sec-title center" style="top:88px">EQUIPMENT WE SUPPLY</h2>
  <p class="sec-sub center" style="top:136px">Precision Equipment for High-Quality Care</p>
  <span class="sec-rule" style="top:183px"></span>

  <div class="equip" style="left:140px;top:221px;width:296px;height:282px">
    <div class="art" style="left:55px;top:25px;width:190px;height:190px" role="img" aria-label="X-ray machine product image"></div>
    <h4 style="top:236px">X-Ray Machine</h4>
  </div>
  <div class="equip" style="left:452px;top:221px;width:607px;height:282px">
    <h4 style="left:27px;width:auto;top:100px;text-align:left">MRI Scanners</h4>
    <p class="abs" style="left:27px;top:144px;width:200px;font-size:10px;line-height:15px;color:#555a78">MRI scan machine or magnetic resonance imaging scan device.</p>
    <div class="btn" style="left:25px;top:198px;width:119px;height:27px;border:1.5px solid var(--blue);color:var(--blue);font-size:9.5px">View Detail</div>
    <div class="art" style="left:290px;top:40px;width:290px;height:210px;border-radius:100px 100px 20px 20px" role="img" aria-label="MRI scanner product image"></div>
  </div>

  <div class="equip" style="left:140px;top:520px;width:296px;height:281px">
    <div class="art" style="left:80px;top:25px;width:136px;height:190px" role="img" aria-label="Infant ventilator product image"></div>
    <h4 style="top:235px">Infant Ventilator</h4>
  </div>
  <div class="equip" style="left:450px;top:520px;width:297px;height:281px">
    <div class="art" style="left:88px;top:25px;width:120px;height:190px" role="img" aria-label="Anesthesia machine product image"></div>
    <h4 style="top:235px">Anesthesia machines</h4>
  </div>
  <div class="equip" style="left:762px;top:520px;width:297px;height:281px">
    <div class="art" style="left:35px;top:40px;width:227px;height:170px" role="img" aria-label="ICU cot product image"></div>
    <h4 style="top:235px">ICU Cots</h4>
  </div>

  <div class="btn btn-navy btn-notch" style="left:497px;top:842px;width:205px;height:41px">Explore All Equipments</div>
</section>

<section class="section empower">
  <div class="abs" style="left:0;top:0;width:620px;height:475px;background:linear-gradient(90deg,#4b5e84,#34497a 70%,rgba(40,55,110,0))" role="img" aria-label="Photograph of medical staff operating a monitoring screen"></div>
  <h2>EMPOWERING<br>YOUR TEAM</h2>
  <p>We offer hands-on training for healthcare professionals, ensuring they are equipped to use the latest medical technologies confidently</p>
  <div class="btn btn-blue" style="left:660px;top:331px;width:140px;height:38px">Learn More</div>
</section>

<section class="section why">
  <h2 class="sec-title center" style="top:90px">WHY ZEROVAN MEDICAL?</h2>
  <p class="sec-sub center" style="top:138px">Your Trusted Medical Supplier</p>
  <span class="sec-rule" style="top:184px"></span>

  <div class="abs" style="left:388px;top:231px;width:417px;height:485px;border-radius:16px;background:linear-gradient(180deg,#f4f7fb,#d9e3ee 70%,#f4f7fb)" role="img" aria-label="Dental treatment chair product image"></div>

  <div class="feature" style="left:181px;top:247px"><div class="ico"><span><svg width="24" height="24" viewBox="0 0 24 24" fill="#fff"><circle cx="8" cy="7" r="3"/><path d="M3 20v-5a5 5 0 0 1 10 0v5z"/><path d="M17 3l1 2 2 .3-1.5 1.4.4 2.1-1.9-1-1.9 1 .4-2.1L14 5.3l2-.3z"/></svg></span></div><h5>Proven Industry<br>Expertise</h5><hr></div>
  <div class="feature" style="left:181px;top:410px"><div class="ico"><span><svg width="24" height="24" viewBox="0 0 24 24" fill="none" stroke="#fff" stroke-width="2.4"><circle cx="12" cy="12" r="7"/><circle cx="12" cy="12" r="2.5" fill="#fff"/></svg></span></div><h5>Complete Service<br>Package</h5><hr></div>
  <div class="feature" style="left:181px;top:584px"><div class="ico"><span><svg width="24" height="24" viewBox="0 0 24 24" fill="#fff"><circle cx="12" cy="8" r="3"/><circle cx="5" cy="10" r="2.3"/><circle cx="19" cy="10" r="2.3"/><path d="M6 20a6 6 0 0 1 12 0zM1 19a4 4 0 0 1 5-4l-1 4zM23 19a4 4 0 0 0-5-4l1 4z"/></svg></span></div><h5>Leading<br>Partners</h5><hr></div>

  <div class="feature" style="left:850px;top:247px"><div class="ico"><span><svg width="24" height="24" viewBox="0 0 24 24" fill="#fff"><path d="M12 2a6 6 0 0 1 4 10.5V15H8v-2.5A6 6 0 0 1 12 2z"/><rect x="9" y="17" width="6" height="3"/></svg></span></div><h5>Comprehensive<br>Solutions</h5><hr></div>
  <div class="feature" style="left:850px;top:410px"><div class="ico"><span><svg width="24" height="24" viewBox="0 0 24 24" fill="#fff"><circle cx="12" cy="7" r="3"/><path d="M6 20a6 6 0 0 1 12 0z"/><circle cx="4" cy="12" r="2"/><circle cx="20" cy="12" r="2"/></svg></span></div><h5>Experienced<br>Team</h5><hr></div>
  <div class="feature" style="left:850px;top:584px"><div class="ico"><span><svg width="24" height="24" viewBox="0 0 24 24" fill="none" stroke="#fff" stroke-width="2.4"><path d="M4 12a8 8 0 1 1 3 6.2L4 20l1-3.5A8 8 0 0 1 4 12z"/></svg></span></div><h5>End-to-End<br>Support</h5><hr></div>

  <div class="btn btn-navy btn-notch" style="left:512px;top:728px;width:175px;height:46px">Go to Catalog</div>
</section>

<section class="section cta">
  <div class="abs" style="inset:0;background:radial-gradient(ellipse at 50% 50%,rgba(255,255,255,.08),rgba(0,0,0,0) 60%)" role="img" aria-label="Faint hospital room photograph in blue overlay"></div>
  <h2 class="abs center">LET’S BRING INNOVATION<br>TO YOUR HEALTHCARE SECTOR</h2>
  <p class="abs center">Contact us for more information on our medical equipment and services.</p>
  <div class="btn btn-white" style="left:516px;top:249px;width:167px;height:40px">Contact Us Now</div>
</section>

<footer class="section footer">
  <div class="brand" style="left:140px;top:84px;font-size:22px"><span class="brand-mark" style="width:30px;height:30px"></span>Zerovan Medical</div>
  <span class="social" style="left:180px"><i></i></span>
  <span class="social" style="left:218px"><i></i></span>
  <span class="social" style="left:256px"><i></i></span>
  <span class="social" style="left:294px"><i></i></span>

  <h6 style="left:417px">Quick Links</h6>
  <ul class="links"><li>Home</li><li>About Us</li><li>Service</li><li>Training</li><li>Project</li></ul>

  <h6 style="left:586px">Contact Us</h6>
  <div class="contact-row" style="top:128px"><svg width="14" height="16" viewBox="0 0 24 24" fill="none" stroke="#2b9ad7" stroke-width="2"><path d="M12 22s7-7 7-12a7 7 0 0 0-14 0c0 5 7 12 7 12z"/><circle cx="12" cy="10" r="2.5"/></svg><span>YOUR LOCATION NAME WILL BE<br>HERE NEAR THIS BUILDING</span></div>
  <div class="contact-row" style="top:180px;font-size:12px;font-weight:600;color:#fff"><svg width="14" height="14" viewBox="0 0 24 24" fill="none" stroke="#2b9ad7" stroke-width="2"><path d="M5 3h4l2 5-3 2a11 11 0 0 0 6 6l2-3 5 2v4a2 2 0 0 1-2 2A17 17 0 0 1 3 5a2 2 0 0 1 2-2z"/></svg><span>0770-555-0142</span></div>
  <div class="contact-row" style="top:216px"><svg width="14" height="14" viewBox="0 0 24 24" fill="none" stroke="#2b9ad7" stroke-width="2"><rect x="3" y="5" width="18" height="14"/><path d="M3 6l9 7 9-7"/></svg><span>info@zerovan-medical.example</span></div>

  <h6 style="left:828px">Subscribe Now</h6>
  <div class="subscribe"><span>Email address...</span><i><svg width="10" height="10" viewBox="0 0 24 24" fill="none" stroke="#fff" stroke-width="3"><path d="M8 4l8 8-8 8"/></svg></i></div>

  <span class="abs" style="left:0;top:320px;width:1200px;height:1px;background:rgba(255,255,255,.1)"></span>
  <p class="abs center copyright">COPYRIGHT © 2024 ZEROVAN MEDICAL. ALL RIGHTS RESERVED.</p>
</footer>

</body>
</html>
```